11X17 Poster Drop A Dress Size Challenge

We are having a 21-Day Drop A Dress Size Challenge for our Fitness Studio. We need a poster designed using the template attached as a reference. I have included our Vorenzo Bootcamps logo to put in the poster as well. Please DO NOT use the graphics in the flyer as we are expecting something much better :)
- Size needed 11x17 with bleeding for printing
- We need this made in Photoshop (CS3 friendly) or at least delivered in PS as we might change some text or re-arrange the design later on.

Target Market(s)

Personal Training Studio

Industry/Entity Type

Printing

Colors
0255a3
3377b5
85acd3
f37123
f68e4e
faa54b
f78f20
0692cd
34a7d8

Requirements
Must have
• Must be 11x17 with bleed for printing
• Must be in PS file (CS3 compatible)
• Must include our Vorenzo Bootcamps logo somewhere in the poster
• Must include the information provided in the attached flyer
Nice to have
• Nice to have quality graphics that coincide with the challenge and our logo
Should not have
• Please NO scantily dressed women :)

```html
<!DOCTYPE html>
<html lang="en">
<head>
<meta charset="utf-8">
<title>Drop a Dress Size in 21 Days – Vorenzo Bootcamps</title>
<link rel="stylesheet" href="https://fonts.googleapis.com/css2?family=Lilita+One&family=Alfa+Slab+One&family=Arvo:wght@400;700&family=Didact+Gothic&family=PT+Sans:wght@700&family=Open+Sans:wght@700&display=swap">
<style>
  :root{
    --orange-light:#f7983f;
    --orange:#ef8129;
    --orange-deep:#cf6420;
    --peach:#fdd3a5;
    --blue:#1d6a9c;
    --blue-ring:#3a9fd6;
    --teal-dark:#1c4b5c;
    --ink:#2a1a10;
    --brown:#3d1d0c;
    --white:#ffffff;
    --scale-grey:#dfe2e6;
  }
  *{box-sizing:border-box;margin:0;padding:0}
  html,body{width:775px;height:1200px;overflow:hidden;background:var(--orange)}
  .poster{
    position:relative;width:775px;height:1200px;overflow:hidden;
    background:radial-gradient(ellipse at 45% 30%,var(--orange-light) 0%,var(--orange) 45%,var(--orange-deep) 100%);
    color:var(--ink);
  }
  .challenge-badge{position:absolute;left:50px;top:50px;width:196px;height:214px}
  .challenge-badge .scale-art{
    position:absolute;inset:0;
    background:linear-gradient(180deg,var(--scale-grey) 0%,#f4f5f6 32%,#f2a45c 42%,var(--orange) 100%);
  }
  .challenge-badge .badge-text{
    position:absolute;left:0;right:0;top:110px;text-align:center;color:var(--white);
    font-family:"PT Sans",sans-serif;font-weight:700;line-height:1;
  }
  .badge-number{font-size:56px;display:block}
  .badge-days{font-size:42px;display:block;margin-top:-2px}
  .badge-word{font-size:31px;display:block;margin-top:4px}
  .headline{position:absolute;left:288px;top:44px;width:470px;text-align:center;color:var(--white);
    text-shadow:2px 3px 0 rgba(90,40,10,.55)}
  .headline .line-1{font-family:"Lilita One",sans-serif;font-size:90px;line-height:1;display:block;letter-spacing:1px}
  .headline .line-2{font-family:"Lilita One",sans-serif;font-size:66px;line-height:1.05;display:block}
  .headline .line-3{font-family:"Alfa Slab One",serif;font-size:62px;line-height:1.15;display:block}
  .intro{position:absolute;left:50px;top:292px;width:690px;font-family:"Didact Gothic",sans-serif;font-size:17px;line-height:1.2;color:var(--ink)}
  .intro p+p{margin-top:17px}
  .offer-lead{position:absolute;left:0;width:775px;top:432px;text-align:center;
    font-family:"Open Sans",sans-serif;font-weight:700;font-size:23px;color:var(--teal-dark)}
  .benefits{position:absolute;left:42px;top:468px;width:690px;height:324px;background:var(--peach);border-radius:10px;
    padding:14px 14px 0 16px;font-family:"PT Sans",sans-serif;font-weight:700;color:var(--ink)}
  .benefits h2{font-size:19px;font-weight:700;margin-bottom:14px}
  .benefits ul{list-style:none;font-size:21px;line-height:1.2}
  .benefits li::before{content:"• "}
  .price-band{position:absolute;left:0;top:820px;width:775px;height:146px;background:var(--blue)}
  .price-band::before,.price-band::after{content:"";position:absolute;left:0;right:0;border-top:2px dashed var(--white)}
  .price-band::before{top:10px}
  .price-band::after{bottom:10px}
  .start-date{position:absolute;left:40px;top:810px;width:176px;height:176px;border-radius:50%;
    background:var(--white);border:7px solid var(--blue-ring);display:flex;align-items:center;justify-content:center}
  .start-date::before{content:"";position:absolute;inset:6px;border-radius:50%;border:2px dotted var(--orange)}
  .start-date p{font-family:"Arvo",serif;font-size:29px;line-height:1.2;color:var(--orange-deep);text-align:center}
  .price-copy{position:absolute;left:240px;top:838px;width:520px;text-align:center;color:var(--white);font-family:"Arvo",serif}
  .price-copy .lead{font-size:23px;display:block}
  .price-copy .deal{font-size:23px;display:block;margin-top:12px}
  .price-copy .bonus{font-size:18px;display:block;margin-top:12px}
  .prize{position:absolute;left:0;width:775px;top:982px;text-align:center;font-family:"Arvo",serif;font-size:20px;color:var(--white)}
  .brand{position:absolute;left:42px;top:1060px;display:flex;align-items:center;gap:12px;
    font-family:"Arvo",serif;font-weight:700;font-size:30px;color:var(--white)}
  .brand .mark{width:22px;height:22px;background:var(--white)}
  .contact{position:absolute;left:370px;top:1034px;width:380px;text-align:center;font-family:"Arvo",serif}
  .contact .hurry{font-size:17px;color:var(--brown)}
  .contact .phone{font-size:36px;color:var(--brown);margin-top:4px;display:block}
  .contact .claim{font-size:12px;color:var(--white);font-weight:700;margin-top:4px;display:block}
  .contact .web{font-size:18px;color:var(--white);font-weight:700;display:block}
</style>
</head>
<body>
<main class="poster">
  <div class="challenge-badge">
    <div class="scale-art" role="img" aria-label="Illustration of a bathroom scale dial above the challenge title"></div>
    <div class="badge-text">
      <span class="badge-number">21</span>
      <span class="badge-days">Days</span>
      <span class="badge-word">Challenge</span>
    </div>
  </div>

  <h1 class="headline">
    <span class="line-1">Drop a</span>
    <span class="line-2">Dress Size</span>
    <span class="line-3">In 21Days</span>
  </h1>

  <div class="intro">
    <p>Are you tired of all the health clubs and fitness centers that tell you  exactly what you want to hear to get you to join, but once you’re a member they forget about you and don’t teach you anything about how to get results?</p>
    <p>Are you frustrated by all the gimmicks; the pills, powders, shakes and gadgets sold on late night TV  that are nothing more than empty promises and slick marketing?</p>
  </div>

  <p class="offer-lead">If so, then this amazing offer is perfect for you...</p>

  <section class="benefits">
    <h2>Here’s what you get:</h2>
    <ul>
      <li>Three weeks worth of Fat Burning Workouts with a Certified Personal Trainer to make sure that you don’t spend one minute exercising that doesn’t produce results.</li>
      <li>21 Days of Fat Burning Meal Plans designed by a Registered Dietician to ensure that you reach your goals as quickly as possible.</li>
      <li>Nutrition Coaching Session to answer all your questions and set you up for success</li>
      <li>21 Days of Lessons to keep you on track to achieving your goal of dropping a dress size</li>
    </ul>
  </section>

  <div class="price-band"></div>
  <div class="start-date"><p>Starts<br>April 6th<br>2015</p></div>
  <div class="price-copy">
    <span class="lead">...You get all this</span>
    <span class="deal">a $327 Value - for ONLY $97!</span>
    <span class="bonus">AND A FREE PHOTO SHOOT! ($150 Value)</span>
  </div>

  <p class="prize">WINNER GETS $100 Cash, A NEW DRESS (Up to $100 Value)</p>

  <div class="brand"><span class="mark"></span><span>Vorenzo Bootcamps</span></div>

  <div class="contact">
    <p class="hurry">HURRY!  SPACE IS LIMITED LADIES!!</p>
    <span class="phone">Call 303-555-0148</span>
    <span class="claim">CLAIM YOUR SPOT NOW</span>
    <span class="web">www.Vorenzobootcamps.com</span>
  </div>
</main>
</body>
</html>
```